hi all

Im after a new age looking business card with my company logo on it

must include these details, I would like the PH and Email to be symbols

If the colours used for card could be kept within the colours used in logo that I have supplied that would be great, if another colour is to be used dark grey would be ok. no light bulbs etc thanks

Details below to be incorporated on card

Damian Holloway

Lic E871302

PH 0219647381

E info@brightvaleelectrical.example.nz

Domestic Commercial Industrial Electricians

```html
<!DOCTYPE html>
<html lang="en">
<head>
<meta charset="utf-8">
<title>Brightvale Electrical – Business Card</title>
<link rel="stylesheet" href="https://fonts.googleapis.com/css2?family=Questrial&display=swap">
<style>
  :root {
    --page-bg: #e6e6e6;
    --card-bg: #f3f3f3;
    --brand-blue: #0a72c0;
    --brand-blue-soft: rgba(10, 114, 192, 0.32);
    --ink-dark: #1e1e1e;
    --text-light: #ffffff;
    --text-body: #1a1a1a;
  }
  * { margin: 0; padding: 0; box-sizing: border-box; }
  html, body {
    width: 1200px;
    height: 900px;
    overflow: hidden;
    background: var(--page-bg);
    font-family: "Questrial", "Century Gothic", sans-serif;
  }
  .business-card {
    position: absolute;
    left: 50px;
    top: 136px;
    width: 1100px;
    height: 628px;
    background: var(--card-bg);
    overflow: hidden;
    box-shadow: 0 10px 30px rgba(0, 0, 0, 0.18);
  }

  /* Header panel: one plain curved edge */
  .header-panel {
    position: absolute;
    inset: 0;
    width: 100%;
    height: 100%;
  }
  .panel-dark { fill: var(--ink-dark); }
  .panel-edge { fill: none; stroke: var(--brand-blue); stroke-width: 22; }

  /* Wave decoration areas: soft fills in the card's tones */
  .wave-decoration {
    position: absolute;
    pointer-events: none;
  }
  .wave-left {
    left: -140px;
    top: 230px;
    width: 520px;
    height: 300px;
    background: radial-gradient(ellipse at 30% 50%, var(--brand-blue-soft), rgba(10, 114, 192, 0) 70%);
  }
  .wave-bottom {
    left: 520px;
    top: 430px;
    width: 640px;
    height: 260px;
    background: radial-gradient(ellipse at 70% 70%, var(--brand-blue-soft), rgba(10, 114, 192, 0) 70%);
  }
  .wave-foot {
    left: 180px;
    top: 520px;
    width: 320px;
    height: 140px;
    background: radial-gradient(ellipse at 50% 80%, var(--brand-blue-soft), rgba(10, 114, 192, 0) 70%);
  }

  .brand-lockup {
    position: absolute;
    left: 40px;
    top: 40px;
    width: 380px;
    text-align: center;
  }
  .brand-ring {
    display: block;
    width: 100px;
    height: 100px;
    margin: 0 auto 16px;
    border: 7px solid var(--ink-dark);
    border-radius: 50%;
  }
  .brand-name {
    font-size: 33px;
    letter-spacing: 2px;
    color: var(--brand-blue);
    text-transform: uppercase;
    white-space: nowrap;
  }

  .holder {
    position: absolute;
    right: 68px;
    top: 54px;
    text-align: right;
    color: var(--text-light);
    font-weight: 700;
  }
  .holder-name { font-size: 44px; line-height: 1.2; }
  .holder-surname { color: var(--brand-blue); }
  .holder-role { font-size: 40px; line-height: 1.45; }

  .contact {
    position: absolute;
    display: flex;
    align-items: center;
    justify-content: flex-end;
    gap: 18px;
    color: var(--text-body);
    font-size: 21px;
    font-weight: 700;
    white-space: nowrap;
  }
  .contact-icon { width: 60px; height: 60px; flex: none; }
  .contact-icon .disc { fill: var(--brand-blue); }
  .contact-icon .glyph { fill: var(--ink-dark); }
  .contact-icon .glyph-cut { fill: var(--brand-blue); }

  .contact-email   { right: 466px; top: 326px; }
  .contact-phone   { right: 129px; top: 326px; }
  .contact-sectors { right: 466px; top: 445px; }
  .contact-licence { right: 129px; top: 445px; }
</style>
</head>
<body>
  <main class="business-card">
    <div class="wave-decoration wave-left" role="img" aria-label="Blue wave decoration"></div>
    <div class="wave-decoration wave-bottom" role="img" aria-label="Blue wave decoration"></div>
    <div class="wave-decoration wave-foot" role="img" aria-label="Blue wave decoration"></div>

    <svg class="header-panel" viewBox="0 0 1100 628" aria-hidden="true">
      <path class="panel-dark" d="M470,0 L1100,0 L1100,255 C940,280 800,250 720,180 C650,120 600,20 470,0Z"/>
      <path class="panel-edge" d="M470,0 C600,20 650,120 720,180 C800,250 940,280 1100,255"/>
    </svg>

    <header class="brand-lockup">
      <span class="brand-ring"></span>
      <p class="brand-name">Brightvale Electrical</p>
    </header>

    <section class="holder">
      <p class="holder-name">Damian <span class="holder-surname">Holloway</span></p>
      <p class="holder-role">CEO</p>
    </section>

    <p class="contact contact-email">
      <span>info@brightvaleelectrical.example.nz</span>
      <svg class="contact-icon" viewBox="0 0 60 60" aria-label="Email">
        <circle class="disc" cx="30" cy="30" r="30"/>
        <rect class="glyph" x="14" y="18" width="32" height="24" rx="3"/>
        <path class="glyph-cut" d="M16,21 L30,32 L44,21 L44,24 L30,35 L16,24Z"/>
      </svg>
    </p>

    <p class="contact contact-phone">
      <span>0219647381</span>
      <svg class="contact-icon" viewBox="0 0 60 60" aria-label="Phone">
        <circle class="disc" cx="30" cy="30" r="30"/>
        <rect class="glyph" x="17" y="13" width="26" height="34" rx="4"/>
        <path class="glyph-cut" d="M34,20 C27,22 27,38 34,40 L35,37 C31,35 31,25 35,23Z"/>
      </svg>
    </p>

    <p class="contact contact-sectors">
      <span>Domestic Comarcial Industrial Ltd</span>
      <svg class="contact-icon" viewBox="0 0 60 60" aria-label="Location">
        <circle class="disc" cx="30" cy="30" r="30"/>
        <rect class="glyph" x="17" y="12" width="26" height="36" rx="4"/>
        <path class="glyph-cut" d="M30,22 C25,22 23,26 23,29 C23,33 30,40 30,40 C30,40 37,33 37,29 C37,26 35,22 30,22Z"/>
        <circle class="glyph" cx="30" cy="29" r="3"/>
      </svg>
    </p>

    <p class="contact contact-licence">
      <span>Lic E871302</span>
      <svg class="contact-icon" viewBox="0 0 60 60" aria-label="Licence">
        <circle class="disc" cx="30" cy="30" r="30"/>
        <rect class="glyph" x="12" y="15" width="36" height="30" rx="2"/>
      </svg>
    </p>
  </main>
</body>
</html>
```